Holvern Incorporated

Holvern is a business that provides consulting, and manages and supplies trades persons in the construction and heavy industries sector. We build, do maintenance, install machinery, and can manage projects or jobs. Would like or prefer more clean, classic designs. Blacks/greys, but open to almost anything.

Target Market(s)

Industrial/Construction/Manufacturing

Industry/Entity Type

Construction Company

Contact Information for Business Card

Clean, business name on the front, possibly have the details on the back, but open to any ideas.

Logo Text

We currently do not have a slogan, open to ideas

Font styles to use
Serif
Sans Serif

Colors

Designer to choose colors to be used in the design.

Requirements
Should not have
• the oval is not my logo, was just an idea. please don't send 20 designs with the oval

```html
<!DOCTYPE html>
<html lang="en">
<head>
<meta charset="utf-8">
<title>Holvern Incorporated — Business Card</title>
<link href="https://fonts.googleapis.com/css2?family=Roboto+Slab:wght@400;500&family=Arimo:wght@400&display=swap" rel="stylesheet">
<style>
  :root {
    --backdrop: #2a2a2b;
    --card-white: #ffffff;
    --card-black: #1c1c1d;
    --ink: #111111;
    --rule: #9a9a9a;
    --reverse-ink: #f2f2f2;
  }
  * { box-sizing: border-box; margin: 0; padding: 0; }
  html, body { width: 1200px; height: 1108px; overflow: hidden; }
  body {
    background: var(--backdrop);
    position: relative;
    font-family: "Arimo", Arial, sans-serif;
  }
  .card {
    position: absolute;
    top: 250px;
    width: 350px;
    height: 600px;
    border-radius: 24px;
    overflow: hidden;
  }
  .card--front {
    left: 200px;
    background: var(--card-white);
    color: var(--ink);
    text-align: center;
  }
  .card--back {
    left: 650px;
    background: var(--card-black);
  }
  .wordmark {
    font-family: "Roboto Slab", Georgia, serif;
    font-weight: 500;
    line-height: 1;
  }
  .card--front .wordmark {
    margin-top: 150px;
    font-size: 68px;
    letter-spacing: -1px;
  }
  .holder-name {
    margin-top: 110px;
    font-family: "Roboto Slab", Georgia, serif;
    font-size: 22px;
    letter-spacing: 0.5px;
  }
  .holder-role {
    margin-top: 4px;
    font-size: 17px;
  }
  .icon-row {
    margin: 12px auto 0;
    width: 280px;
    display: flex;
    align-items: center;
    gap: 8px;
  }
  .icon-row .rule { flex: 1; height: 1px; background: var(--rule); }
  .icon-row svg { display: block; }
  .contact-list {
    margin-top: 12px;
    font-size: 18px;
    line-height: 1.3;
    list-style: none;
  }
  .divider {
    width: 260px;
    height: 1px;
    background: var(--rule);
    margin: 12px auto;
  }
  .address { font-size: 18px; line-height: 1.3; }
  .back-texture {
    position: absolute;
    inset: 0;
    background: linear-gradient(160deg, #262627 0%, #1f1f20 55%, #1a1a1b 100%);
  }
  .card--back .wordmark {
    position: absolute;
    left: 180px;
    top: 420px;
    font-size: 30px;
    color: var(--reverse-ink);
  }
</style>
</head>
<body>
  <section class="card card--front" aria-label="Card front">
    <div class="wordmark">Holvern</div>
    <h1 class="holder-name">MARCUS ELLERY</h1>
    <p class="holder-role">Managing Director</p>
    <div class="icon-row">
      <span class="rule"></span>
      <svg width="24" height="24" viewBox="0 0 24 24" aria-label="Phone"><rect width="24" height="24" rx="5" fill="#111"/><path d="M7 6c1-1 2 0 3 2s-1 2 0 3l2 2c1 1 1-1 3 0s3 2 2 3-3 2-6-1-6-6-4-9z" fill="#fff"/></svg>
      <svg width="24" height="24" viewBox="0 0 24 24" aria-label="Email"><rect width="24" height="24" rx="5" fill="#111"/><rect x="5" y="7" width="14" height="10" fill="none" stroke="#fff" stroke-width="1.6"/><path d="M5 7l7 6 7-6" fill="none" stroke="#fff" stroke-width="1.6"/></svg>
      <svg width="24" height="24" viewBox="0 0 24 24" aria-label="Location"><rect width="24" height="24" rx="5" fill="#111"/><path d="M12 19s-5-5-5-9a5 5 0 0 1 10 0c0 4-5 9-5 9z" fill="#fff"/><circle cx="12" cy="10" r="2" fill="#111"/></svg>
      <span class="rule"></span>
    </div>
    <ul class="contact-list">
      <li>044-218 730 561</li>
      <li>hello@holvern.com</li>
      <li>www.holvern.com</li>
    </ul>
    <div class="divider"></div>
    <p class="address">87, Foundry Lane East,<br>30918, Westmarch</p>
  </section>

  <section class="card card--back" aria-label="Card back">
    <div class="back-texture" role="img" aria-label="Faint repeated company name pattern across the dark card"></div>
    <div class="wordmark">Holvern</div>
  </section>
</body>
</html>
```